Construction Machinery Company : needs two pages flyers to advertise "Demolition Tools"

>>UPDATE BRIEF

Hi Mr./ Ms, Designers,

To make your design work easier,
- I have updated the instruction (Please see attachment file 5 "Brief" , or below "Requirement session")
- I also re-upload the attachments. They are all photos and content for the design. Very Clear now.
- I have also increased the budget.

*More information, please go
www.quartz-ridge.com/spikeline

Hope you can work on my project.

>>Previous Brief
Hi Mr./ Ms. Designers,

We are an international construction machinery distributors, located in Hong Kong. Our client is HONG KONG contractors.
We want to start marketing "demolition tool" - the metal tool that used on excavator breaker.

We want the final designs export to two products
1) two pages A4 size flyers (Front for products, and Back for company info.)
2) one page 360mm x 265mm size advertisement (grouping products and company information together)
* design can be the same.

Requirement:
1) Tone: As construction industry is a very "man" industry, we want the flyer is very "METAL" theme.
(Our Company theme colour is RED, but you can use a new colour"

2) Theme: I want customer know we are PROFESSIONAL, SPECIALIST moil point seller, and we have a lot of experience.

3) Product message: we want the messages are
-TOUGHER,
-LONGER LIFE,
-LOWER PRICE,
-CONVENIENCE DELIVERY

4) Product: there are four kinds of "demolition tool", Moil Point, Wedge, Blunt, Cone. But I want to emphasis "Moil Point".

Remarks:
- To let you know what demolition tool is,
I have attached photos [teaching] for your reference.

- Beside the Product photos, we may put supplier's factory photos as background, to show it is a big factory.

- I have put many photo, as Source and for Reference.
Feel free to ask me questions.

- We may put "Chinese word" beside English in the end. I can send you the FONT file later.

Our website page:
http://quartz-ridge.com/spikeline/

Learning Reference:
http://www.brovantools.com/tools-parts.html

Target Market(s)

[Hong Kong] Construction Contractor user.

Industry/Entity Type

Construction Company

Requirements
Must have
• Theme: Since construction is a very "man" industry, Please have the theme "man and neat"
• two pages A4 size flyers

```html
<!DOCTYPE html>
<html lang="en">
<head>
<meta charset="utf-8">
<title>Quartz Ridge – Demolition Tools Brochure Spread</title>
<link rel="stylesheet" href="https://fonts.googleapis.com/css2?family=Open+Sans:wght@400;600;700&display=swap">
<style>
  :root {
    --backdrop: #9c9c9c;
    --paper: #f4f4f4;
    --paper-shade: #e3e3e3;
    --panel: #e9e9e9;
    --panel-edge: #d2d2d2;
    --ink: #3a3a3a;
    --ink-soft: #6d6d6d;
    --charcoal: #2a2a2a;
    --brand-red: #d4202c;
    --brand-red-dark: #8e1219;
    --stripe: #cfcfcf;
  }
  * { box-sizing: border-box; margin: 0; padding: 0; }
  html, body { width: 1200px; height: 900px; overflow: hidden; }
  body {
    background: var(--backdrop);
    font-family: "Open Sans", Arial, sans-serif;
    color: var(--ink);
    position: relative;
  }
  .spread {
    position: absolute;
    left: 40px; top: 252px;
    width: 1120px; height: 396px;
    display: flex;
    box-shadow: 0 10px 30px rgba(0,0,0,.25);
  }
  .page {
    position: relative;
    width: 560px; height: 396px;
    overflow: hidden;
    background: linear-gradient(180deg, #fafafa 0%, var(--paper) 55%, var(--paper-shade) 100%);
  }
  .page--left { border-right: 1px solid #d8d8d8; }

  /* shared red footer band */
  .footer-band {
    position: absolute; left: 0; right: 0; bottom: 0; height: 12px;
    background: linear-gradient(180deg, var(--brand-red) 0%, var(--brand-red-dark) 100%);
  }
  .footer-band::before {
    content: ""; position: absolute; left: 0; right: 0; top: -3px; height: 3px;
    background: #bdbdbd;
  }

  .top-stripe { position: absolute; left: 0; top: 0; width: 560px; height: 60px; }

  /* left page */
  .section-title {
    position: absolute; left: 0; top: 20px;
    width: 190px; height: 40px;
  }
  .section-title__text {
    position: absolute; left: 34px; top: 4px;
    font-size: 24px; font-weight: 400; color: #fff; letter-spacing: .3px;
  }
  .intro-copy {
    position: absolute; left: 44px; top: 84px; width: 470px;
    font-size: 7.4px; line-height: 1.6; color: var(--ink-soft);
  }
  .intro-copy p + p { margin-top: 8px; }
  .world-map {
    position: absolute; left: 92px; top: 172px;
    width: 290px; height: 130px;
    background: radial-gradient(ellipse at 50% 50%, #8d8d8d 0%, #b3b3b3 55%, rgba(200,200,200,0) 75%);
    opacity: .8;
  }
  .brand {
    position: absolute; display: flex; align-items: center; gap: 6px;
    font-weight: 700; font-size: 13px; color: var(--charcoal); letter-spacing: .5px;
  }
  .brand__dot {
    width: 16px; height: 16px; border-radius: 50%;
    border: 2px solid var(--brand-red);
  }
  .brand--left { left: 28px; bottom: 28px; }
  .page-url {
    position: absolute; right: 26px; bottom: 22px;
    font-size: 7px; color: var(--ink-soft); font-weight: 600;
  }

  /* right page */
  .feature-columns {
    position: absolute; left: 0; top: 52px; right: 0; bottom: 15px;
    display: flex;
  }
  .feature {
    flex: 1; position: relative;
    background: linear-gradient(180deg, #e2e2e2 0%, var(--panel) 60%, #f3f3f3 100%);
    border-right: 2px solid #f7f7f7;
    box-shadow: inset -1px 0 0 var(--panel-edge);
  }
  .feature:last-child { border-right: 0; }
  .feature__photo {
    position: absolute; left: 50%; top: 78px; transform: translateX(-50%);
    width: 118px; height: 118px; border-radius: 50%;
    border: 3px solid var(--brand-red);
    box-shadow: 0 2px 6px rgba(0,0,0,.25);
  }
  .feature__photo--tools { background: radial-gradient(circle, #6b6b6b 0%, #2f3132 100%); }
  .feature__photo--stock { background: radial-gradient(circle, #e07a45 0%, #b8522b 70%, #8b8b8b 100%); }
  .feature__photo--factory { background: radial-gradient(circle, #a09a90 0%, #6a625c 70%, #4d4a48 100%); }
  .feature__marker {
    position: absolute; left: 24px; top: 68px;
    width: 18px; height: 18px; border-radius: 50%;
    background: var(--brand-red);
  }
  .feature__caption {
    position: absolute; left: 0; right: 0; top: 214px;
    text-align: center; font-size: 8px; font-weight: 700;
    color: var(--brand-red); letter-spacing: .6px; line-height: 1.3;
  }
  .brand--right {
    right: 24px; top: 14px; flex-direction: column; gap: 2px; font-size: 12px;
  }
  .brand--right .brand__dot { width: 20px; height: 20px; }
  .page-url--right { right: 22px; bottom: 24px; }
</style>
</head>
<body>
  <main class="spread">
    <!-- Left page: introduction -->
    <section class="page page--left">
      <svg class="top-stripe" viewBox="0 0 560 60" aria-hidden="true">
        <defs>
          <linearGradient id="stripeFade" x1="0" x2="1">
            <stop offset="0" stop-color="#bdbdbd"/>
            <stop offset="1" stop-color="#e4e4e4"/>
          </linearGradient>
        </defs>
        <polygon points="170,22 560,10 560,24 178,36" fill="url(#stripeFade)"/>
      </svg>
      <svg class="section-title" viewBox="0 0 190 40" aria-hidden="true">
        <defs>
          <linearGradient id="titleBand" x1="0" y1="0" x2="0" y2="1">
            <stop offset="0" stop-color="#4a4a4a"/>
            <stop offset="1" stop-color="#1f1f1f"/>
          </linearGradient>
        </defs>
        <polygon points="0,4 190,0 174,36 0,40" fill="url(#titleBand)"/>
        <rect x="0" y="4" width="22" height="36" fill="#3a3a3a"/>
        <rect x="14" y="8" width="6" height="28" fill="var(--brand-red)"/>
      </svg>
      <h1 class="section-title__text" style="position:absolute;left:34px;top:24px;font-size:24px;font-weight:400;color:#fff;">Introduction</h1>

      <div class="intro-copy">
        <p>QR manufactures the widest range of high quality demolition tools in Hong Kong, compatible with most hydraulic heavy duty breakers. Engineers at QR are doing their best in manufacturing process, quality control and R&amp;D to produce the highest quality demolition tools in the world. QR tools are manufactured only with the highest quality materials and our workmanship undergoes all heat treatment technology to ensure outstanding performance and durability. The tools are made in our factory, equipped with the most cutting edge technology around for our customers.</p>
        <p>We at QR guarantee customer satisfaction from the high quality of our products. Please do not hesitate to contact us when you are interested in our tools.</p>
      </div>

      <div class="world-map" role="img" aria-label="Dotted world map marking Hong Kong"></div>

      <div class="brand brand--left"><span class="brand__dot"></span>QUARTZ RIDGE</div>
      <span class="page-url">quartz-ridge.com</span>
      <div class="footer-band"></div>
    </section>

    <!-- Right page: key features -->
    <section class="page page--right">
      <div class="feature-columns">
        <article class="feature">
          <span class="feature__marker"></span>
          <div class="feature__photo feature__photo--tools" role="img" aria-label="Photo of stacked moil point tools"></div>
          <p class="feature__caption">TOUGHER STEEL</p>
        </article>
        <article class="feature">
          <span class="feature__marker"></span>
          <div class="feature__photo feature__photo--stock" role="img" aria-label="Photo of painted demolition tools in stock"></div>
          <p class="feature__caption">LONGER LIFE</p>
        </article>
        <article class="feature">
          <span class="feature__marker"></span>
          <div class="feature__photo feature__photo--factory" role="img" aria-label="Photo of the factory floor"></div>
          <p class="feature__caption">CONVENIENT<br>DELIVERY</p>
        </article>
      </div>
      <svg class="top-stripe" viewBox="0 0 560 60" aria-hidden="true">
        <polygon points="0,10 230,22 224,36 0,26" fill="url(#stripeFade)"/>
      </svg>
      <div class="brand brand--right"><span class="brand__dot"></span>QUARTZ RIDGE</div>
      <span class="page-url page-url--right">quartz-ridge.com</span>
      <div class="footer-band"></div>
    </section>
  </main>
</body>
</html>
```